Korvane blockchain

A Blockchain investment company template for a switzerland based company. The company is also offering its own blockchain infrastructure in partnership with a top 200 blockchain project, on which blockchain startups can develop their ideas.
In addition, co-working spaces are offered in an innovation center.
So these three parts should be covered in the template

1. Crypto investment
2. Offering the blockchain infrastructure
3. Co-working spaces (https://travelnix.example/)

Target Market(s)

Blockchain / Crypto

Colors
ec1f27

Requirements
Must have
• Connection to the three parts mentioned in the description
inculding to logo attached
Nice to have
• connection to switzerland

```html
<!DOCTYPE html>
<html lang="en">
<head>
<meta charset="utf-8">
<title>Korvane blockchain – presentation template</title>
<link href="https://fonts.googleapis.com/css2?family=Montserrat:wght@300;400;500;600;700;800&family=Poppins:wght@300;400;500;600;700&display=swap" rel="stylesheet">
<style>
:root{
  --red:#ec1f27;
  --ink:#1b1b1d;
  --dark:#1e1f22;
  --dark-2:#2a2b2f;
  --muted:#6b6b70;
  --line:#dcdcdf;
  --canvas:#e9eaec;
  --pink:#fbe4e5;
  --card-border:#f2b9bb;
}
*{box-sizing:border-box;margin:0;padding:0}
html,body{width:1200px;height:4392px;overflow:hidden}
body{background:var(--canvas);font-family:'Poppins',sans-serif;color:var(--ink);position:relative}
.stage{position:absolute;left:0;top:0;width:1200px;height:770px;background:linear-gradient(180deg,#a6aaaf 0%,#c6c9cd 70%,var(--canvas) 100%)}
.hero{transform:scale(1.26);transform-origin:left top;left:251px;top:190px;box-shadow:0 20px 40px rgba(0,0,0,.25)}
.slide{position:absolute;width:554px;height:310px;overflow:hidden;background:#fff}
.slide.dark{background:var(--dark);color:#fff}
.col-l{left:26px}.col-r{left:620px}
.abs{position:absolute}
.head{font-family:'Montserrat',sans-serif;font-weight:600;line-height:1.15}
.txt{font-size:5.4px;line-height:1.5;color:var(--muted)}
.dark .txt,.txt.light{color:#b9b9be}
.red{color:var(--red)}
.white{color:#fff}
.center{text-align:center}
.mark{position:absolute;left:9px;top:8px;font:700 6.5px 'Montserrat',sans-serif;color:var(--red)}
.copy{position:absolute;left:7px;top:110px;writing-mode:vertical-rl;transform:rotate(180deg);font:500 4px 'Montserrat',sans-serif;letter-spacing:1px;color:#a0a0a5}
.pg{position:absolute;left:8px;bottom:8px;width:11px;height:11px;border-radius:50%;background:var(--red);color:#fff;font:600 4.5px 'Poppins',sans-serif;display:flex;align-items:center;justify-content:center}
.pill{position:absolute;background:var(--red);color:#fff;border-radius:12px;display:flex;align-items:center;justify-content:center;font-family:'Montserrat',sans-serif;font-weight:700}
.brand{position:absolute;display:flex;align-items:center;gap:6px;font-family:'Montserrat',sans-serif;font-weight:700;color:var(--red)}
.brand .sq{border:2px solid var(--red)}
.photo{position:absolute}
.bullets{position:absolute;list-style:none}
.bullets li{position:relative;padding-left:9px;font-size:5.4px;line-height:1.5;color:var(--muted);margin-bottom:5px}
.bullets li::before{content:"";position:absolute;left:0;top:2px;width:5px;height:5px;border-radius:50%;background:var(--red)}
.dark .bullets li{color:#d0d0d4}
.agenda{position:absolute;left:300px;top:60px;width:190px;list-style:none}
.agenda li{display:flex;gap:12px;font-size:6px;color:#555;border-bottom:1px solid var(--line);padding:4px 0 4px}
.agenda li span{color:var(--red);width:12px}
.card{position:absolute;width:150px;height:75px;border:1px solid var(--card-border);border-radius:5px;background:#fff;box-shadow:0 3px 8px rgba(236,31,39,.08)}
.card svg{position:absolute;left:10px;top:16px}
.card .name{position:absolute;left:45px;top:12px;font-size:6.8px;font-weight:600}
.card .txt{position:absolute;left:45px;top:23px;width:95px}
.item{position:absolute;width:215px}
.item .dot{position:absolute;left:0;top:0;width:22px;height:22px;border-radius:50%;background:var(--red);display:flex;align-items:center;justify-content:center}
.item .name{position:absolute;left:32px;top:0;font-size:6.8px;font-weight:600}
.item .txt{position:absolute;left:32px;top:10px;width:170px}
.crypto-card{position:absolute;top:185px;width:100px;height:100px;background:var(--dark-2);border:1px solid #3a3b40;padding:8px}
.crypto-card .name{font-size:6.2px;font-weight:600;margin:7px 0 3px}
.partner-box{position:absolute;left:52px;width:460px;height:40px;border:1px solid var(--card-border);border-radius:3px}
.partner-box svg{position:absolute;left:9px;top:10px}
.partner-box .name{position:absolute;left:42px;top:6px;font-size:6.5px;font-weight:600}
.partner-box .txt{position:absolute;left:42px;top:16px;width:400px}
.badge{position:absolute;width:58px;height:30px;background:#fff;border:1px solid #eee;border-radius:3px;box-shadow:0 2px 5px rgba(0,0,0,.12);display:flex;align-items:center;justify-content:center}
.data{position:absolute;left:55px;top:100px;width:455px;border-collapse:collapse;font-size:5.5px;text-align:center;color:#555}
.data th{background:var(--red);color:#fff;height:16px;font-weight:600}
.data th.blank{background:transparent}
.data td{height:23px;border-bottom:1px solid var(--line)}
.data td.label{background:var(--dark);color:#fff;font-weight:600;width:120px;border-bottom:1px solid #3a3b40}
.tick{color:var(--red);font-size:9px;font-weight:700}
.stat{position:absolute;width:120px;text-align:center}
.stat b{display:block;font-family:'Montserrat',sans-serif;font-size:22px;font-weight:800;color:var(--red);letter-spacing:1px}
.tl-label{position:absolute;width:90px;text-align:center}
.tl-label b{display:block;font-size:6.5px;font-weight:600}
.contact{position:absolute;left:50px;display:flex;align-items:center;gap:7px;font-size:6px;color:#e2e2e6}
.contact i{width:9px;height:9px;border-radius:50%;background:var(--red);display:block}
</style>
</head>
<body>

<section class="stage" aria-label="Title slide preview"></section>
<section class="slide hero">
  <div class="photo" role="img" aria-label="Hand holding a crypto coin on a dark background" style="left:0;top:0;width:554px;height:240px;background:radial-gradient(ellipse at 78% 40%,#6a5a52 0%,#3a3234 35%,#1d1b1e 75%)"></div>
  <div class="pill" style="left:44px;top:52px;width:150px;height:16px;font-size:6.5px;letter-spacing:1.5px">WWW.WEBSITENAME.COM</div>
  <div class="abs head white" style="left:40px;top:106px;font-size:37px;font-weight:800">PRESENTATION</div>
  <div class="abs head white" style="left:40px;top:146px;font-size:25px;font-weight:700">TITLE GOES HERE</div>
  <div class="abs white" style="left:40px;top:174px;font-size:15px;font-weight:300;letter-spacing:2px">Sub Title Goes Here</div>
  <div class="pill" style="left:410px;top:228px;width:160px;height:22px;font-size:7px">March 2021</div>
  <div class="brand" style="left:32px;top:262px;font-size:15px"><span class="sq" style="width:20px;height:20px"></span>Korvane blockchain</div>
</section>

<section class="slide col-l" style="top:801px">
  <div class="abs" style="left:0;top:0;width:554px;height:3px;background:var(--red)"></div>
  <div class="brand" style="left:0;width:554px;justify-content:center;top:38px;font-size:11px">Korvane blockchain</div>
  <div class="abs head center" style="left:0;width:554px;top:116px;font-size:38px;font-weight:800;line-height:1">PRESENTATION</div>
  <div class="abs head center" style="left:0;width:554px;top:153px;font-size:26px;font-weight:700;line-height:1">TITLE GOES HERE</div>
  <div class="abs center red" style="left:0;width:554px;top:179px;font-size:15px;font-weight:300;letter-spacing:2px">Sub Title Goes Here</div>
  <div class="pill" style="left:208px;top:236px;width:138px;height:20px;font-size:9px;font-weight:500;font-family:'Poppins',sans-serif">Presenter Name</div>
  <div class="abs" style="left:0;top:300px;width:554px;height:4px;background:var(--red)"></div>
</section>

<section class="slide col-r" style="top:801px">
  <div class="photo" role="img" aria-label="Hiker in a red jacket facing a snowy mountain peak" style="left:0;top:0;width:250px;height:310px;background:linear-gradient(180deg,#f4f6f8 0%,#dfe5eb 40%,#a9b3bd 75%,#7d8791 100%)"></div>
  <div class="brand" style="left:250px;top:72px;font-size:10px">Korvane blockchain</div>
  <div class="abs head" style="left:250px;top:125px;font-size:31px;font-weight:800;line-height:1">PRESENTATION</div>
  <div class="abs head" style="left:250px;top:156px;font-size:22px;font-weight:700;line-height:1">TITLE GOES HERE</div>
  <div class="abs red" style="left:250px;top:180px;font-size:11px;font-weight:300;letter-spacing:2px">Sub Title Goes Here</div>
  <div class="abs" style="left:250px;top:212px;font-size:5.5px;font-weight:600;letter-spacing:1px">WWW.WEBSITE.COM</div>
</section>

<section class="slide col-l dark" style="top:1125px">
  <div class="photo" role="img" aria-label="Dark snowy alpine mountain range" style="left:0;top:0;width:554px;height:310px;background:linear-gradient(180deg,#2a2b2f 0%,#3f4146 45%,#1a1b1e 100%)"></div>
  <div class="brand" style="left:34px;top:62px;font-size:16px;color:#fff"><span class="sq" style="width:22px;height:22px"></span>Korvane blockchain</div>
  <div class="abs head white" style="left:32px;top:138px;font-size:37px;font-weight:700;line-height:1">Presentation</div>
  <div class="abs head white" style="left:32px;top:176px;font-size:26px;font-weight:700;line-height:1">Title Goes Here</div>
  <div class="abs red" style="left:32px;top:203px;font-size:15px;font-weight:300;letter-spacing:2px">Sub Title Goes Here</div>
  <div class="pill" style="left:32px;top:262px;width:138px;height:16px;font-size:6.5px;letter-spacing:1px">WWW.WEBSITENAME.COM</div>
</section>

<section class="slide col-r" style="top:1125px">
  <div class="photo" role="img" aria-label="Hand holding a crypto coin on a dark background" style="left:0;top:0;width:554px;height:240px;background:radial-gradient(ellipse at 78% 40%,#6a5a52 0%,#3a3234 35%,#1d1b1e 75%)"></div>
  <div class="pill" style="left:44px;top:52px;width:150px;height:16px;font-size:6.5px;letter-spacing:1.5px">WWW.WEBSITENAME.COM</div>
  <div class="abs head white" style="left:40px;top:106px;font-size:37px;font-weight:800">PRESENTATION</div>
  <div class="abs head white" style="left:40px;top:146px;font-size:25px;font-weight:700">TITLE GOES HERE</div>
  <div class="abs white" style="left:40px;top:174px;font-size:15px;font-weight:300;letter-spacing:2px">Sub Title Goes Here</div>
  <div class="pill" style="left:410px;top:228px;width:160px;height:22px;font-size:7px">March 2021</div>
  <div class="brand" style="left:32px;top:262px;font-size:15px"><span class="sq" style="width:20px;height:20px"></span>Korvane blockchain</div>
</section>

<section class="slide col-l" style="top:1450px">
  <div class="mark">Korvane</div><div class="copy">COPYRIGHT © 2021</div><div class="pg">03</div>
  <div class="abs head" style="left:65px;top:108px;width:160px;font-size:19px">Here Goes Title Of Your Agenda</div>
  <div class="abs red" style="left:65px;top:188px;font-size:7.5px;font-weight:600">Here Goes A Short Subtitle</div>
  <ol class="agenda">
    <li><span>i.</span>Introduction</li>
    <li><span>ii.</span>About Us</li>
    <li><span>iii.</span>Welcome Message</li>
    <li><span>iv.</span>Company Profile</li>
    <li><span>v.</span>Team</li>
    <li><span>vi.</span>Team Group</li>
    <li><span>vii.</span>Portfolio</li>
    <li><span>viii.</span>Info graphic</li>
    <li><span>ix.</span>Contact Us</li>
  </ol>
</section>

<section class="slide col-r" style="top:1450px">
  <div class="mark">Korvane</div><div class="copy">COPYRIGHT © 2021</div><div class="pg">04</div>
  <div class="abs head" style="left:45px;top:25px;font-size:18px">Here Goes Title Of This Slide</div>
  <div class="abs head" style="left:290px;top:180px;font-size:46px;font-weight:800;color:var(--pink)">Korvane</div>
</section>

<section class="slide col-l" style="top:1776px">
  <div class="mark">Korvane</div><div class="copy">COPYRIGHT © 2021</div><div class="pg">05</div>
  <div class="abs" style="left:420px;top:0;width:134px;height:310px;background:var(--red)"></div>
  <div class="photo" role="img" aria-label="Modern innovation centre building below alpine peaks" style="left:290px;top:70px;width:238px;height:165px;border-radius:6px;background:linear-gradient(180deg,#b9cbe0 0%,#d7dde3 45%,#8a9097 70%,#5b6066 100%)"></div>
  <div class="abs head" style="left:48px;top:55px;width:220px;font-size:20px">Das Basecamp für Innovationen.</div>
  <div class="abs red" style="left:48px;top:106px;font-size:7.5px;font-weight:600">Eine Welt für Kreativität &amp; Begegnung.</div>
  <p class="abs txt" style="left:48px;top:122px;width:210px">Lorem ipsum dolor sit amet, consectetur adipiscing elit, sed do eiusmod tempor incididunt ut labore et dolore magna aliqua. Ut enim ad minim veniam, quis nostrud exercitation ullamco laboris nisi ut aliquip ex ea commodo consequat. Duis aute irure dolor in reprehenderit in voluptate velit esse cillum dolore eu fugiat nulla.</p>
  <ul class="bullets" style="left:48px;top:206px;width:220px">
    <li>Lorem ipsum dolor sit amet, consectetur adipiscing</li>
    <li>Sed do eiusmod tempor incididunt ut labore et</li>
    <li>Dolore magna aliqua ut enim ad minim veniam</li>
    <li>Quis nostrud exercitation ullamco laboris nisi ut</li>
  </ul>
</section>

<section class="slide col-r" style="top:1776px">
  <div class="mark">Korvane</div><div class="copy">COPYRIGHT © 2021</div><div class="pg">06</div>
  <div class="abs head center" style="left:0;width:554px;top:38px;font-size:20px;font-weight:500">Co-working spaces</div>
  <div class="abs red center" style="left:0;width:554px;top:64px;font-size:7px;font-weight:600">Here Is a Place for subtitle</div>
  <p class="abs txt" style="left:65px;top:105px;width:210px">Lorem ipsum dolor sit amet, consectetur adipiscing elit, sed do eiusmod tempor incididunt ut labore et dolore magna aliqua. Ut enim ad minim veniam, quis nostrud exercitation ullamco laboris nisi ut aliquip. Lorem ipsum dolor sit amet, sed do eiusmod tempor incididunt ut labore et dolore magna aliqua.</p>
  <ul class="bullets" style="left:300px;top:105px;width:200px">
    <li>Lorem ipsum dolor sit amet, consectetur adipiscing</li>
    <li>Sed do eiusmod tempor incididunt ut labore et</li>
    <li>Dolore magna aliqua ut enim ad minim veniam</li>
    <li>Quis nostrud exercitation ullamco laboris nisi ut</li>
  </ul>
  <div class="photo" role="img" aria-label="Open co-working hall with red accents" style="left:35px;top:180px;width:160px;height:90px;background:linear-gradient(135deg,#e9e6e4,#b9b1ad 60%,#8c5f5c)"></div>
  <div class="photo" role="img" aria-label="Innovation centre exterior with mountains" style="left:200px;top:180px;width:168px;height:90px;background:linear-gradient(180deg,#c3d2e2,#a3a9ae 55%,#6d7278)"></div>
  <div class="photo" role="img" aria-label="Bright atrium with wooden stairs" style="left:373px;top:180px;width:160px;height:90px;background:linear-gradient(135deg,#efe6da,#c9a77f 55%,#8d6a48)"></div>
</section>

<section class="slide col-l dark" style="top:2100px">
  <div class="photo" role="img" aria-label="Hand holding a golden crypto coin" style="left:0;top:0;width:230px;height:310px;background:radial-gradient(ellipse at 45% 55%,#c7a47a 0%,#6f5a4a 35%,#2b2a2c 75%)"></div>
  <div class="abs head white" style="left:258px;top:58px;font-size:20px;font-weight:500">Cryptocurrency</div>
  <p class="abs txt light" style="left:258px;top:92px;width:268px">Lorem ipsum dolor sit amet, consectetur adipiscing elit, sed do eiusmod tempor incididunt ut labore et dolore magna aliqua. Lorem ipsum dolor sit amet, consectetur adipiscing elit. Sed do eiusmod tempor incididunt ut labore et dolore magna aliqua. Ut enim ad minim veniam, quis nostrud exercitation ullamco laboris nisi ut aliquip.</p>
  <div class="crypto-card" style="left:205px">
    <svg width="16" height="16" viewBox="0 0 16 16"><circle cx="8" cy="8" r="7" fill="none" stroke="#fff" stroke-width="1.2"/><path d="M6 4v8M6 4h3a2 2 0 010 4H6h3.5a2 2 0 010 4H6" fill="none" stroke="#fff" stroke-width="1"/></svg>
    <div class="name">Currency</div>
    <p class="txt light">Lorem ipsum dolor sit amet, consectetur adipiscing elit, sed do eiusmod tempor ut labore et dolore magna aliqua.</p>
  </div>
  <div class="crypto-card" style="left:312px">
    <svg width="16" height="16" viewBox="0 0 16 16"><rect x="2" y="3" width="12" height="10" rx="1" fill="none" stroke="#fff" stroke-width="1.2"/><path d="M5 7h6M5 10h4" stroke="#fff" stroke-width="1"/></svg>
    <div class="name">Dedication</div>
    <p class="txt light">Lorem ipsum dolor sit amet, consectetur adipiscing elit, sed do eiusmod tempor ut labore et dolore magna aliqua.</p>
  </div>
  <div class="crypto-card" style="left:419px">
    <svg width="16" height="16" viewBox="0 0 16 16"><circle cx="5" cy="9" r="3" fill="none" stroke="#fff" stroke-width="1.2"/><circle cx="11" cy="9" r="3" fill="none" stroke="#fff" stroke-width="1.2"/></svg>
    <div class="name">Customer Focus</div>
    <p class="txt light">Lorem ipsum dolor sit amet, consectetur adipiscing elit, sed do eiusmod tempor ut labore et dolore magna aliqua.</p>
  </div>
</section>

<section class="slide col-r dark" style="top:2100px">
  <div class="mark">Korvane</div><div class="copy">COPYRIGHT © 2021</div><div class="pg">08</div>
  <div class="abs" style="left:0;top:0;width:4px;height:310px;background:var(--red)"></div>
  <div class="abs white center" style="left:40px;width:170px;top:108px;font-size:8.5px;font-weight:500">GET TO KNOW</div>
  <div class="abs head red center" style="left:40px;width:170px;top:118px;font-size:42px;font-weight:500;line-height:1">SCO</div>
  <div class="abs white center" style="left:50px;width:150px;top:166px;font-size:7px;line-height:1.35">a smart contract model that shares project tokens with network stakers</div>
  <div class="abs white" style="left:250px;top:32px;font-size:12px;font-weight:400">STAKERS</div>
  <ul class="bullets" style="left:250px;top:52px;width:280px">
    <li>Receive tokens from selected partner projects</li>
    <li>Staked assets stay in your own wallet at all times</li>
    <li>Pick from a wide range of projects and reward types</li>
  </ul>
  <p class="abs txt light" style="left:250px;top:125px;width:282px">SCO is a flexible approach to staking rewards that benefits both projects and token holders, and it is drawing growing interest from professional investors.</p>
  <p class="abs txt light" style="left:250px;top:160px;width:282px">The model combines market dynamics, staking based rewards, community feedback and early token distribution. Exchanges, staking services, funds and incubators are now exploring what this model can bring to young blockchain projects and the wider industry.</p>
</section>

<section class="slide col-l" style="top:2426px">
  <div class="mark">Korvane</div><div class="copy">COPYRIGHT © 2021</div><div class="pg">09</div>
  <div class="abs head" style="left:45px;top:50px;font-size:23px">Here Goes</div>
  <div class="abs head red" style="left:45px;top:78px;font-size:23px">Title Of This Slide</div>
  <div class="abs" style="left:45px;top:145px;font-size:7.5px;font-weight:600">Your Short Text Here</div>
  <div class="abs" style="left:45px;top:160px;width:470px;height:1px;background:var(--line)"></div>
  <div class="abs" style="left:45px;top:159px;width:60px;height:2px;background:var(--red)"></div>
  <p class="abs txt" style="left:45px;top:172px;width:150px">Lorem ipsum dolor sit amet, consectetur adipiscing elit, sed do eiusmod tempor incididunt ut labore et dolore magna aliqua. Lorem ipsum dolor sit amet.<br><br>Sed do eiusmod tempor incididunt ut labore et dolore magna aliqua.<br><br>Ut enim ad minim veniam, quis nostrud exercitation ullamco laboris nisi ut aliquip.</p>
  <p class="abs txt" style="left:212px;top:172px;width:150px">Lorem ipsum dolor sit amet, consectetur adipiscing elit, sed do eiusmod tempor incididunt ut labore et dolore magna aliqua.<br><br>Consectetur adipiscing elit, sed do eiusmod tempor incididunt ut labore et dolore magna aliqua.<br><br>Ut enim ad minim veniam, quis nostrud exercitation.</p>
  <p class="abs txt" style="left:380px;top:172px;width:150px">Lorem ipsum dolor sit amet, consectetur adipiscing elit, sed do eiusmod tempor incididunt ut labore et dolore magna aliqua.<br><br>Consectetur adipiscing elit, sed do eiusmod tempor incididunt ut labore et dolore magna aliqua.<br><br>Ut enim ad minim veniam, quis nostrud aliquip.</p>
</section>

<section class="slide col-r" style="top:2426px">
  <div class="mark">Korvane</div><div class="copy">COPYRIGHT © 2021</div><div class="pg">10</div>
  <div class="abs head" style="left:55px;top:42px;font-size:20px">Your Title Here</div>
  <div class="card" style="left:48px;top:95px"><svg width="24" height="24" viewBox="0 0 24 24"><circle cx="12" cy="12" r="5" fill="none" stroke="var(--red)" stroke-width="1.5"/><path d="M12 2v4M12 18v4M2 12h4M18 12h4M5 5l3 3M16 16l3 3M5 19l3-3M16 8l3-3" stroke="var(--red)" stroke-width="1.5"/></svg><div class="name">Project name</div><p class="txt">Lorem Ipsum is simply dummy unknown printer took a galley of type and scrambled it to make.</p></div>
  <div class="card" style="left:208px;top:95px"><svg width="24" height="24" viewBox="0 0 24 24"><circle cx="9" cy="8" r="4" fill="none" stroke="var(--red)" stroke-width="1.5"/><path d="M3 21c0-5 12-5 12 0M15 13l6 6" stroke="var(--red)" stroke-width="1.5" fill="none"/></svg><div class="name">Project name</div><p class="txt">Lorem Ipsum is simply dummy unknown printer took a galley of type and scrambled it to make.</p></div>
  <div class="card" style="left:368px;top:95px"><svg width="24" height="24" viewBox="0 0 24 24"><rect x="3" y="4" width="18" height="16" rx="2" fill="none" stroke="var(--red)" stroke-width="1.5"/><path d="M7 15l3-4 3 3 4-5" stroke="var(--red)" stroke-width="1.5" fill="none"/></svg><div class="name">Project name</div><p class="txt">Lorem Ipsum is simply dummy unknown printer took a galley of type and scrambled it to make.</p></div>
  <div class="card" style="left:48px;top:190px"><svg width="24" height="24" viewBox="0 0 24 24"><circle cx="12" cy="12" r="9" fill="none" stroke="var(--red)" stroke-width="1.5"/><path d="M12 6v6l4 3" stroke="var(--red)" stroke-width="1.5" fill="none"/></svg><div class="name">Project name</div><p class="txt">Lorem Ipsum is simply dummy unknown printer took a galley of type and scrambled it to make.</p></div>
  <div class="card" style="left:208px;top:190px"><svg width="24" height="24" viewBox="0 0 24 24"><circle cx="7" cy="8" r="3" fill="none" stroke="var(--red)" stroke-width="1.5"/><circle cx="17" cy="8" r="3" fill="none" stroke="var(--red)" stroke-width="1.5"/><path d="M2 20c0-4 10-4 10 0M12 20c0-4 10-4 10 0" stroke="var(--red)" stroke-width="1.5" fill="none"/></svg><div class="name">Project name</div><p class="txt">Lorem Ipsum is simply dummy unknown printer took a galley of type and scrambled it to make.</p></div>
  <div class="card" style="left:368px;top:190px"><svg width="24" height="24" viewBox="0 0 24 24"><path d="M12 3a6 6 0 00-4 10.5V17h8v-3.5A6 6 0 0012 3zM9 20h6" stroke="var(--red)" stroke-width="1.5" fill="none"/></svg><div class="name">Project name</div><p class="txt">Lorem Ipsum is simply dummy unknown printer took a galley of type and scrambled it to make.</p></div>
</section>

<section class="slide col-l" style="top:2751px">
  <div class="mark">Korvane</div><div class="copy">COPYRIGHT © 2021</div><div class="pg">11</div>
  <div class="abs head" style="left:55px;top:38px;font-size:20px">Your Title Here</div>
  <div class="item" style="left:55px;top:90px"><div class="dot"><svg width="12" height="12" viewBox="0 0 12 12"><circle cx="6" cy="6" r="3" fill="none" stroke="#fff" stroke-width="1.2"/></svg></div><div class="name">Project name</div><p class="txt">Lorem ipsum dolor sit amet, nec an dictas equidem appellantur, ut has commune accommodare. Mea illum, ludus solet idpro.</p></div>
  <div class="item" style="left:295px;top:90px"><div class="dot"><svg width="12" height="12" viewBox="0 0 12 12"><rect x="2" y="2" width="8" height="8" fill="none" stroke="#fff" stroke-width="1.2"/></svg></div><div class="name">Project name</div><p class="txt">Lorem ipsum dolor sit amet, nec an dictas equidem appellantur, ut has commune accommodare. Mea illum, ludus solet idpro.</p></div>
  <div class="item" style="left:55px;top:150px"><div class="dot"><svg width="12" height="12" viewBox="0 0 12 12"><path d="M2 9l3-4 2 2 3-4" fill="none" stroke="#fff" stroke-width="1.2"/></svg></div><div class="name">Project name</div><p class="txt">Lorem ipsum dolor sit amet, nec an dictas equidem appellantur, ut has commune accommodare. Mea illum, ludus solet idpro.</p></div>
  <div class="item" style="left:295px;top:150px"><div class="dot"><svg width="12" height="12" viewBox="0 0 12 12"><circle cx="6" cy="6" r="4" fill="none" stroke="#fff" stroke-width="1.2"/><path d="M6 3v3l2 1" stroke="#fff" fill="none"/></svg></div><div class="name">Project name</div><p class="txt">Lorem ipsum dolor sit amet, nec an dictas equidem appellantur, ut has commune accommodare. Mea illum, ludus solet idpro.</p></div>
  <div class="item" style="left:55px;top:210px"><div class="dot"><svg width="12" height="12" viewBox="0 0 12 12"><path d="M6 2l4 8H2z" fill="none" stroke="#fff" stroke-width="1.2"/></svg></div><div class="name">Project name</div><p class="txt">Lorem ipsum dolor sit amet, nec an dictas equidem appellantur, ut has commune accommodare. Mea illum, ludus solet idpro.</p></div>
  <div class="item" style="left:295px;top:210px"><div class="dot"><svg width="12" height="12" viewBox="0 0 12 12"><path d="M2 6h8M6 2v8" stroke="#fff" stroke-width="1.2"/></svg></div><div class="name">Project name</div><p class="txt">Lorem ipsum dolor sit amet, nec an dictas equidem appellantur, ut has commune accommodare. Mea illum, ludus solet idpro.</p></div>
</section>

<section class="slide col-r" style="top:2751px">
  <div class="mark">Korvane</div><div class="copy">COPYRIGHT © 2021</div><div class="pg">12</div>
  <div class="photo" role="img" aria-label="Dark misty mountain landscape" style="left:0;top:0;width:554px;height:160px;background:linear-gradient(180deg,#2b2c30 0%,#45474c 55%,#222326 100%)"></div>
  <div class="abs head white center" style="left:0;width:554px;top:36px;font-size:18px">Here Add Awesome Text</div>
  <div class="abs red center" style="left:0;width:554px;top:58px;font-size:8px;font-weight:600;font-style:italic">Write here a great subtitle</div>
  <p class="abs txt light center" style="left:77px;top:78px;width:400px">Lorem ipsum dolor sit amet, consectetur adipiscing elit, sed do eiusmod tempor incididunt ut labore et dolore magna aliqua. Lorem ipsum dolor sit amet, consectetur adipiscing elit.</p>
  <svg class="abs" style="left:0;top:0" width="554" height="310" viewBox="0 0 554 310">
    <g fill="var(--red)" stroke="#fff" stroke-width="3"><circle cx="115" cy="160" r="22"/><circle cx="277" cy="160" r="22"/><circle cx="440" cy="160" r="22"/></g>
    <g fill="none" stroke="#fff" stroke-width="1.4"><circle cx="115" cy="160" r="8"/><circle cx="115" cy="160" r="3"/><path d="M271 166l12-12M277 154h6v6"/><rect x="433" y="153" width="14" height="14" rx="2"/></g>
  </svg>
  <div class="abs center" style="left:55px;width:120px;top:196px;font-size:7px;font-weight:600">Project name</div>
  <p class="abs txt" style="left:55px;width:120px;top:208px">Lorem ipsum dolor sit amet, nec an dictas equidem appellantur, ut has the same but eco commune accommodare. Mea illum, ludus solet idpro.</p>
  <div class="abs center" style="left:217px;width:120px;top:196px;font-size:7px;font-weight:600">Project name</div>
  <p class="abs txt" style="left:217px;width:120px;top:208px">Lorem ipsum dolor sit amet, nec an dictas equidem appellantur, ut has the same but eco commune accommodare. Mea illum, ludus solet idpro.</p>
  <div class="abs center" style="left:380px;width:120px;top:196px;font-size:7px;font-weight:600">Project name</div>
  <p class="abs txt" style="left:380px;width:120px;top:208px">Lorem ipsum dolor sit amet, nec an dictas equidem appellantur, ut has the same but eco commune accommodare. Mea illum, ludus solet idpro.</p>
</section>

<section class="slide col-l" style="top:3075px">
  <div class="mark">Korvane</div><div class="copy">COPYRIGHT © 2021</div><div class="pg">13</div>
  <div class="abs" style="left:30px;top:150px;width:270px;height:150px;background:var(--dark)"></div>
  <div class="abs head" style="left:48px;top:52px;width:170px;font-size:19px">Place for the ScreenShot</div>
  <div class="abs red" style="left:48px;top:103px;font-size:7px;font-weight:400">No problem is too big or too small!</div>
  <div class="abs red" style="left:48px;top:113px;font-size:7px;font-weight:600">We're here to help.</div>
  <p class="abs txt light" style="left:45px;top:182px;width:195px">Lorem ipsum dolor sit amet, consectetur adipiscing elit, sed do eiusmod tempor incididunt ut labore et dolore magna aliqua. Lorem ipsum dolor sit amet, consectetur adipiscing elit, sed do eiusmod tempor incididunt ut labore et dolore magna aliqua. Ut enim ad minim veniam, quis nostrud exercitation ullamco laboris nisi ut aliquip.</p>
  <div class="abs" style="left:290px;top:68px;width:240px;height:158px;background:#151517;border-radius:5px;padding:6px">
    <div role="img" aria-label="Screenshot of a mining rig with a crypto coin" style="width:100%;height:100%;background:radial-gradient(ellipse at 60% 55%,#a58a62 0%,#4a4447 35%,#1f1e22 75%)"></div>
  </div>
  <div class="abs" style="left:278px;top:226px;width:265px;height:6px;background:#c9c9cd;border-radius:0 0 6px 6px"></div>
</section>

<section class="slide col-r" style="top:3075px">
  <div class="mark">Korvane</div><div class="copy">COPYRIGHT © 2021</div><div class="pg">14</div>
  <div class="abs head center" style="left:0;width:554px;top:45px;font-size:20px;font-weight:500">Here Goes Title Of This Slide</div>
  <p class="abs txt center" style="left:77px;top:95px;width:400px">Lorem Ipsum the printing and typesetting industry. Lorem Ipsum has been the industry's standard dummy text ever since the 1500s, when an unknown printer took a galley of type and scrambled it to make a type specimen book. It has survived not only five centuries.</p>
  <div class="stat" style="left:68px;top:160px"><b>1M</b><p class="txt">Lorem Ipsum has been the industry's standard dummy text ever since the 1500s</p></div>
  <div class="stat" style="left:217px;top:160px"><b>2021</b><p class="txt">Lorem Ipsum has been the industry's standard dummy text ever since</p></div>
  <div class="stat" style="left:366px;top:160px"><b>150+</b><p class="txt">Lorem Ipsum has been the industry's standard dummy text ever since the 1500s</p></div>
</section>

<section class="slide col-l" style="top:3400px">
  <div class="mark">Korvane</div><div class="copy">COPYRIGHT © 2021</div><div class="pg">15</div>
  <div class="abs head" style="left:52px;top:28px;font-size:19px">Our Partner</div>
  <div class="abs head" style="left:182px;top:30px;font-size:16px;font-weight:700">Nodeweave</div>
  <div class="partner-box" style="top:70px"><svg width="20" height="20" viewBox="0 0 20 20"><circle cx="10" cy="10" r="4" fill="none" stroke="var(--red)" stroke-width="1.4"/><path d="M10 1v4M10 15v4M1 10h4M15 10h4" stroke="var(--red)" stroke-width="1.4"/></svg><div class="name">Build Faster On The Nodeweave Network</div><p class="txt">A modular network that gives young teams the tools to test and launch their ideas quickly, with low running costs and clear guides for every step of development.</p></div>
  <div class="partner-box" style="top:115px"><svg width="20" height="20" viewBox="0 0 20 20"><rect x="3" y="7" width="14" height="10" fill="none" stroke="var(--red)" stroke-width="1.4"/><path d="M3 7l4-4h6l4 4" fill="none" stroke="var(--red)" stroke-width="1.4"/></svg><div class="name">Nodeweave Launchpad</div><p class="txt">A simple dashboard where startups set up their own network, choose the features they need and go live without writing the core infrastructure themselves.</p></div>
  <div class="partner-box" style="top:160px"><svg width="20" height="20" viewBox="0 0 20 20"><rect x="3" y="3" width="14" height="14" rx="2" fill="none" stroke="var(--red)" stroke-width="1.4"/><path d="M7 10h6M10 7v6" stroke="var(--red)" stroke-width="1.4"/></svg><div class="name">Nodeweave Starter Kit</div><p class="txt">A ready-made base network for first prototypes. Teams can adapt it to their use case step by step and add new functions as their product grows.</p></div>
  <div class="partner-box" style="top:205px"><svg width="20" height="20" viewBox="0 0 20 20"><path d="M10 2v16M2 10h16" stroke="var(--red)" stroke-width="1.4"/><circle cx="10" cy="10" r="7" fill="none" stroke="var(--red)" stroke-width="1.4"/></svg><div class="name">Network Bridge</div><p class="txt">Links projects built with Korvane to other networks so that data and assets can move safely between ecosystems and partners.</p></div>
</section>

<section class="slide col-r" style="top:3400px">
  <div class="mark">Korvane</div><div class="copy">COPYRIGHT © 2021</div><div class="pg">16</div>
  <div class="abs head" style="left:45px;top:140px;font-size:19px;font-weight:500">Unsere Partner</div>
  <div class="badge" style="left:250px;top:45px"><span style="width:36px;height:6px;background:#d43a3a;border-radius:3px"></span></div>
  <div class="badge" style="left:317px;top:45px"><span style="width:34px;height:8px;background:#7cbf4a;border-radius:4px"></span></div>
  <div class="badge" style="left:384px;top:45px"><span style="width:32px;height:8px;background:#2c3f78"></span></div>
  <div class="badge" style="left:451px;top:45px"><span style="width:12px;height:12px;background:#1b1b1d;border-radius:50%"></span></div>
  <div class="badge" style="left:250px;top:91px"><span style="width:30px;height:7px;background:#3a3a3a"></span></div>
  <div class="badge" style="left:317px;top:91px"><span style="width:34px;height:7px;background:#2f5aa8"></span></div>
  <div class="badge" style="left:384px;top:91px"><span style="width:20px;height:14px;background:#1f4fa0"></span></div>
  <div class="badge" style="left:451px;top:91px"><span style="width:34px;height:10px;background:#e0432f;border-radius:2px"></span></div>
  <div class="badge" style="left:250px;top:137px"><span style="width:14px;height:14px;background:#e24a3b;border-radius:50%"></span></div>
  <div class="badge" style="left:317px;top:137px"><span style="width:34px;height:8px;background:#222"></span></div>
  <div class="badge" style="left:384px;top:137px"><span style="width:30px;height:6px;background:#c9a14a"></span></div>
  <div class="badge" style="left:451px;top:137px"><span style="width:14px;height:14px;background:#e5a12e;border-radius:50%"></span></div>
  <div class="badge" style="left:250px;top:183px"><span style="width:30px;height:8px;background:#2a4d8f"></span></div>
  <div class="badge" style="left:317px;top:183px"><span style="width:36px;height:6px;background:#d43a3a;border-radius:3px"></span></div>
  <div class="badge" style="left:384px;top:183px"><span style="width:32px;height:8px;background:#2c3f78"></span></div>
  <div class="badge" style="left:451px;top:183px"><span style="width:12px;height:12px;background:#1b1b1d;border-radius:50%"></span></div>
  <div class="badge" style="left:250px;top:229px"><span style="width:30px;height:7px;background:#3a3a3a"></span></div>
  <div class="badge" style="left:317px;top:229px"><span style="width:34px;height:7px;background:#2f5aa8"></span></div>
  <div class="badge" style="left:384px;top:229px"><span style="width:20px;height:14px;background:#1f4fa0"></span></div>
  <div class="badge" style="left:451px;top:229px"><span style="width:34px;height:10px;background:#e0432f;border-radius:2px"></span></div>
</section>

<section class="slide col-l" style="top:3726px">
  <div class="mark">Korvane</div><div class="copy">COPYRIGHT © 2021</div><div class="pg">17</div>
  <div class="abs head" style="left:45px;top:30px;font-size:19px;font-weight:500">Here Goes Title Of This Slide</div>
  <table class="data">
    <thead><tr><th class="blank"></th><th>Your Text Here</th><th>Your Text Here</th><th>Your Text Here</th><th>Your Text Here</th></tr></thead>
    <tbody>
      <tr><td class="label">You can replace this text</td><td>1250</td><td class="tick">✓</td><td>50%</td><td>1250</td></tr>
      <tr><td class="label">You can replace this text</td><td>3623</td><td class="tick">✕</td><td>30%</td><td>3623</td></tr>
      <tr><td class="label">You can replace this text</td><td>2569</td><td class="tick">✓</td><td>12%</td><td>2569</td></tr>
      <tr><td class="label">You can replace this text</td><td>1020</td><td class="tick">✕</td><td>65%</td><td>1020</td></tr>
      <tr><td class="label">You can replace this text</td><td>2320</td><td class="tick">✓</td><td>36%</td><td>2320</td></tr>
      <tr><td class="label">You can replace this text</td><td>3698</td><td class="tick">✕</td><td>95%</td><td>3698</td></tr>
    </tbody>
  </table>
</section>

<section class="slide col-r" style="top:3726px">
  <div class="mark">Korvane</div><div class="copy">COPYRIGHT © 2021</div><div class="pg">18</div>
  <div class="abs head" style="left:55px;top:30px;font-size:19px;font-weight:500">Here Goes Title Of This Slide</div>
  <svg class="abs" style="left:0;top:0" width="554" height="310" viewBox="0 0 554 310">
    <polygon points="55,145 135,145 143,152 135,159 55,159" fill="var(--red)"/>
    <polygon points="140,145 228,145 236,152 228,159 140,159 148,152" fill="var(--dark)"/>
    <polygon points="233,145 321,145 329,152 321,159 233,159 241,152" fill="var(--red)"/>
    <polygon points="326,145 414,145 422,152 414,159 326,159 334,152" fill="var(--dark)"/>
    <polygon points="419,145 515,145 515,159 419,159 427,152" fill="var(--red)"/>
    <g font-family="Montserrat,sans-serif" font-size="7.5" font-weight="700" fill="#fff" text-anchor="middle">
      <text x="95" y="155">1990</text><text x="188" y="155">2001</text><text x="281" y="155">2010</text><text x="374" y="155">2018</text><text x="467" y="155">2021</text>
    </g>
    <g stroke="#888" stroke-width="0.8" fill="none">
      <path d="M95 125v16M92 138l3 3 3-3"/><path d="M281 125v16M278 138l3 3 3-3"/><path d="M467 125v16M464 138l3 3 3-3"/>
      <path d="M188 180v-16M185 167l3-3 3 3"/><path d="M374 180v-16M371 167l3-3 3 3"/>
    </g>
  </svg>
  <div class="tl-label" style="left:50px;top:95px"><b>Your Title</b><p class="txt">Refers to a good or service being offered</p></div>
  <div class="tl-label" style="left:236px;top:95px"><b>Your Title</b><p class="txt">Refers to a good or service being offered</p></div>
  <div class="tl-label" style="left:422px;top:95px"><b>Your Title</b><p class="txt">Refers to a good or service being offered</p></div>
  <div class="tl-label" style="left:143px;top:184px"><b>Your Title</b><p class="txt">Refers to a good or service being offered</p></div>
  <div class="tl-label" style="left:329px;top:184px"><b>Your Title</b><p class="txt">Refers to a good or service being offered</p></div>
</section>

<section class="slide col-l" style="top:4052px">
  <div class="mark">Korvane</div><div class="copy">COPYRIGHT © 2021</div><div class="pg">19</div>
  <div class="abs head" style="left:60px;top:28px;font-size:19px;font-weight:500">Here Goes Title Of This Slide</div>
  <svg class="abs" style="left:0;top:0" width="554" height="310" viewBox="0 0 554 310">
    <g transform="translate(282 185)" stroke="#fff" stroke-width="3">
      <path d="M0 0V-75A75 75 0 0 1 75 0Z" fill="var(--dark)"/>
      <path d="M0 0H75A75 75 0 0 1 0 75Z" fill="var(--red)"/>
      <path d="M0 0V75A75 75 0 0 1 -75 0Z" fill="var(--dark)"/>
      <path d="M0 0H-75A75 75 0 0 1 0 -75Z" fill="var(--red)"/>
      <circle r="38" fill="#fff" stroke="none"/>
      <g fill="#fff" stroke="none"><circle cx="-40" cy="-40" r="10"/><circle cx="40" cy="-40" r="10"/><circle cx="40" cy="40" r="10"/><circle cx="-40" cy="40" r="10"/></g>
      <g fill="none" stroke="var(--red)" stroke-width="1.2"><circle cx="-40" cy="-40" r="4"/><path d="M36 -36l8-8M40 -44h4v4"/><rect x="36" y="36" width="8" height="8"/><path d="M-44 40h8M-40 36v8"/></g>
    </g>
    <text x="282" y="188" text-anchor="middle" font-family="Montserrat,sans-serif" font-size="7" font-weight="700" fill="var(--red)">Korvane blockchain</text>
  </svg>
  <div class="abs" style="left:70px;top:100px;width:120px;text-align:right"><div style="font-size:6.5px;font-weight:600">Your Contents Here</div><p class="txt">Lorem ipsum dolor sit amet, consectetur adipiscing elit, sed do eiusmod tempor incididunt.</p></div>
  <div class="abs" style="left:70px;top:215px;width:120px;text-align:right"><div style="font-size:6.5px;font-weight:600">Your Contents Here</div><p class="txt">Lorem ipsum dolor sit amet, consectetur adipiscing elit, sed do eiusmod tempor incididunt.</p></div>
  <div class="abs" style="left:375px;top:100px;width:120px"><div style="font-size:6.5px;font-weight:600">Your Contents Here</div><p class="txt">Lorem ipsum dolor sit amet, consectetur adipiscing elit, sed do eiusmod tempor incididunt.</p></div>
  <div class="abs" style="left:375px;top:215px;width:120px"><div style="font-size:6.5px;font-weight:600">Your Contents Here</div><p class="txt">Lorem ipsum dolor sit amet, consectetur adipiscing elit, sed do eiusmod tempor incididunt.</p></div>
</section>

<section class="slide col-r dark" style="top:4052px">
  <div class="photo" role="img" aria-label="Dark snowy mountain range at dusk" style="left:0;top:0;width:554px;height:310px;background:linear-gradient(180deg,#2a2b2f 0%,#46484d 50%,#1b1c1f 100%)"></div>
  <div class="abs head white" style="left:50px;top:92px;font-size:24px;font-weight:500">Thank You.</div>
  <div class="abs head red" style="left:50px;top:122px;font-size:24px;font-weight:500">Contact Us.</div>
  <div class="contact" style="top:168px"><i></i>www.travelnix.example</div>
  <div class="contact" style="top:184px"><i></i>contact@travelnix.example</div>
  <div class="contact" style="top:200px"><i></i>+41 00 000 00 00</div>
  <div class="contact" style="top:216px"><i></i>Here is a place for address</div>
  <div class="brand" style="left:275px;top:190px;font-size:20px"><span class="sq" style="width:26px;height:26px"></span>Korvane blockchain</div>
</section>

</body>
</html>
```